Fast quick flyer for Merchant Showcase Fair

I am an information security consultant that needs to have a flyer and QUICK!!!
I need to get it to the printer today to have if done by monday. Quick turnaound.
I don't need the most amazing flyer but something that will capture their attention and offer them 40% off my base rate.
Updates

Here's some slight updates to the text, can you update and incorporate (PS: For some reason, when I initially put in Luvaro Systems, a " (quote) showed up, it's an apostrophe ( Luvaro Systems): Text: Luvaro Systems is the information security department for small and mid-sized businesses. Leveraging our 20+ years of information security experience, we will bring you the same level of service found at Pinnacle 400 companies. Small and mid-sized companies are often the target of malicious activity because they tend to lack the expertise to properly secure their environments. Now you can have your very own information security department at a fraction of the cost of a full time staff. Our typical rate for our premium offering: Shieldwise Direct is $5000/month based on a signed one year commitment. But for expo attendees, we are offering a special discount. As an expo attendee, you are eligible for a 40% discount. Shieldwise Direct for expo attendees will be $3000/month based on a signed one year commitment. Why put your company and your business at risk. Luvaro Systems is here to secure your company's future! Contact us now for more information: Martin Kessell Luvaro Systems "The information security department of small and mid-sized companies" 555-318-7702 info@luvarosys.example http://www.luvarosys.example

Also, this is going to be a 6x9 heavy stock postcard

Addition: Promo Code: TradeFairPass 2014

Target Market(s)

Small businesses with a small IT department that can't afford to hire a full time IT Security Staff. We are the outsourced Information Security group

Industry/Entity Type

Small Business

Colors

Designer to choose colors to be used in the design.

Requirements
Must have
• Sell the idea that they need to take security serious and that we are the ones to do the job

Should stress that because they are attendees of the Merchant Showcase Fair, they are eligible to get a 40% discount on our standard rate

```html
<!DOCTYPE html>
<html lang="en">
<head>
<meta charset="utf-8">
<title>Luvaro Systems – Merchant Showcase Fair Postcard</title>
<link rel="stylesheet" href="https://fonts.googleapis.com/css2?family=Lato:wght@400;700;900&family=Cinzel:wght@500&display=swap">
<style>
  :root {
    --ink-dark: #0b0d10;
    --ink-mid: #22272d;
    --ink-glow: #3a4148;
    --text-light: #ffffff;
    --brand-gold: #8c8457;
    --seal-light: #a9adb2;
    --seal-dark: #6d7176;
  }
  * { margin: 0; padding: 0; box-sizing: border-box; }
  html, body { width: 1200px; height: 846px; overflow: hidden; background: var(--ink-dark); }
  .postcard {
    position: relative;
    width: 1200px;
    height: 846px;
    overflow: hidden;
    font-family: "Lato", Arial, sans-serif;
    color: var(--text-light);
  }
  .backdrop {
    position: absolute;
    inset: 0;
    background:
      radial-gradient(ellipse 360px 420px at 560px 360px, var(--ink-glow) 0%, rgba(40,45,52,0.55) 45%, transparent 100%),
      radial-gradient(ellipse 700px 600px at 600px 420px, var(--ink-mid) 0%, var(--ink-dark) 100%);
  }
  .brand {
    position: absolute;
    left: 78px;
    top: 78px;
    display: flex;
    align-items: center;
    gap: 14px;
  }
  .brand-mark {
    width: 48px;
    height: 48px;
    background: var(--brand-gold);
  }
  .brand-name {
    font-family: "Cinzel", Georgia, serif;
    font-weight: 500;
    font-size: 40px;
    line-height: 1;
    letter-spacing: 1px;
    color: var(--brand-gold);
    text-transform: uppercase;
  }
  .offer-seal {
    position: absolute;
    right: 10px;
    top: 20px;
    width: 220px;
    height: 220px;
  }
  .offer-seal text { font-family: "Lato", Arial, sans-serif; fill: var(--text-light); }
  .headline {
    position: absolute;
    top: 218px;
    left: 0;
    width: 100%;
    text-align: center;
    font-weight: 900;
    font-size: 56px;
    line-height: 66px;
  }
  .pitch {
    position: absolute;
    top: 440px;
    left: 0;
    width: 100%;
    text-align: center;
    font-weight: 700;
    font-size: 25px;
    line-height: 37px;
  }
  .pitch p + p { margin-top: 35px; }
  .contact-person, .contact-web {
    position: absolute;
    bottom: 44px;
  }
  .contact-person { left: 60px; }
  .contact-web { right: 66px; text-align: left; }
  .contact-name, .contact-phone {
    font-weight: 700;
    font-size: 40px;
    line-height: 44px;
  }
  .contact-email, .contact-url {
    font-size: 18px;
    line-height: 22px;
  }
</style>
</head>
<body>
<main class="postcard">
  <div class="backdrop" role="img" aria-label="Dark photo of a businessman in a suit touching a glowing virtual screen of technology icons"></div>

  <div class="brand">
    <span class="brand-mark"></span>
    <span class="brand-name">Luvaro Systems</span>
  </div>

  <svg class="offer-seal" viewBox="0 0 220 220" aria-label="Special Expo Rate 40% off, regular price $5,000.00">
    <defs>
      <linearGradient id="sealFill" x1="0" y1="0" x2="0" y2="1">
        <stop offset="0" stop-color="var(--seal-light)"/>
        <stop offset="1" stop-color="var(--seal-dark)"/>
      </linearGradient>
    </defs>
    <g transform="translate(110 110)" fill="url(#sealFill)">
      <rect x="-74" y="-74" width="148" height="148"/>
      <rect x="-74" y="-74" width="148" height="148" transform="rotate(15)"/>
      <rect x="-74" y="-74" width="148" height="148" transform="rotate(30)"/>
      <rect x="-74" y="-74" width="148" height="148" transform="rotate(45)"/>
      <rect x="-74" y="-74" width="148" height="148" transform="rotate(60)"/>
      <rect x="-74" y="-74" width="148" height="148" transform="rotate(75)"/>
      <circle r="86" fill="none" stroke="#ffffff" stroke-opacity="0.5" stroke-width="1.5" stroke-dasharray="3 3"/>
    </g>
    <text x="110" y="92" text-anchor="middle" font-size="13" font-weight="700">Special Expo Rate</text>
    <text x="110" y="134" text-anchor="middle" font-size="40" font-weight="900">40% OFF</text>
    <text x="110" y="152" text-anchor="middle" font-size="8" font-weight="400">REGULAR PRICE $5,000.00</text>
  </svg>

  <h1 class="headline">Information security<br>department for small<br>and mid-sized businesses</h1>

  <div class="pitch">
    <p>Small companies are targets because they lack the expertise at<br>information security that large companies have.</p>
    <p>We have over 20 years of information security experience and<br>we can leverage our expertise to give small companies the same<br>level of security experience that Pinnacle 400 companies have.</p>
  </div>

  <div class="contact-person">
    <div class="contact-name">Martin Kessell</div>
    <div class="contact-email">martin.kessell@luvarosys.example</div>
  </div>

  <div class="contact-web">
    <div class="contact-phone">555-318-7702</div>
    <div class="contact-url">http://www.luvarosys.example</div>
  </div>
</main>
</body>
</html>
```